Zielgruppe
Wir sind ein klassisches IT Systemhaus und betreuen in unserer Region kleine und mittelständische Unternehmen sowie öffentliche Einrichtungen.
Aufgabenstellung
Es soll ein modernes Desigm, eine moderne Menüführung vorhanden sein. Dabei soll ein Megamenü eingebunden werden

```html
<!DOCTYPE html>
<html lang="de">
<head>
<meta charset="utf-8">
<title>Managed IT-Services – nexora</title>
<link rel="stylesheet" href="https://fonts.googleapis.com/css2?family=Work+Sans:wght@400;500;600;700&display=swap">
<style>
  :root {
    --white: #ffffff;
    --ink: #222631;
    --ink-soft: #3a3f4b;
    --cyan: #22dfe6;
    --cyan-soft: #b9eef0;
    --violet: #4a30e2;
    --violet-glass: rgba(74, 48, 226, 0.92);
    --page-bg: #eff0f6;
    --accent-field: #e3e5ee;
    --hero-dark: #1f2a2c;
    --hero-mid: #3d4a4c;
    --photo-dark: #1e2a3a;
    --photo-mid: #4a5e78;
  }
  * { box-sizing: border-box; margin: 0; padding: 0; }
  html, body {
    width: 1200px; height: 900px; overflow: hidden;
    font-family: "Work Sans", sans-serif; color: var(--ink);
    background: var(--page-bg);
  }
  .site-header {
    position: absolute; left: 0; top: 0; width: 1200px; height: 65px;
    background: var(--white); border-top: 2px solid var(--ink);
  }
  .brand {
    position: absolute; left: 29px; top: 10px;
    display: flex; align-items: center; gap: 9px;
    font-size: 31px; font-weight: 500; color: var(--ink); letter-spacing: 0.3px;
  }
  .brand-dot { width: 34px; height: 34px; border-radius: 50%; background: var(--cyan); }
  .main-nav { position: absolute; top: 0; left: 0; height: 65px; }
  .nav-item {
    position: absolute; top: 23px; font-size: 15px; font-weight: 500; color: var(--ink-soft);
    display: flex; align-items: center; gap: 8px; white-space: nowrap;
  }
  .nav-item svg { width: 9px; height: 6px; }
  .nav-item.is-active { color: var(--cyan); }
  .search-icon { position: absolute; left: 886px; top: 24px; width: 15px; height: 15px; }
  .quote-button {
    position: absolute; left: 920px; top: 11px; width: 141px; height: 44px;
    background: var(--cyan); color: var(--white); font-size: 15px; font-weight: 700;
    display: flex; align-items: center; justify-content: center;
    box-shadow: 0 6px 16px rgba(34, 223, 230, 0.25);
  }
  .hero {
    position: absolute; left: 0; top: 65px; width: 1200px; height: 262px;
    background: linear-gradient(110deg, var(--hero-dark) 0%, #2a3637 45%, var(--hero-mid) 70%, #7d8482 100%);
  }
  .hero-title-box {
    position: absolute; left: 285px; top: 119px; width: 519px; height: 106px;
    background: var(--violet-glass); color: var(--white); text-align: center;
  }
  .hero-title { margin-top: 20px; font-size: 34px; font-weight: 600; line-height: 40px; }
  .breadcrumb { margin-top: 8px; font-size: 15px; font-weight: 600; }
  .breadcrumb span { margin: 0 6px; }
  .service-menu {
    position: absolute; left: 28px; top: 459px; width: 327px; height: 361px;
    background: var(--white); padding: 44px 0 0 45px;
    box-shadow: 0 20px 40px rgba(60, 70, 110, 0.08);
  }
  .service-menu h2 { font-size: 21px; font-weight: 600; margin-bottom: 26px; }
  .service-menu ul { list-style: none; }
  .service-menu li { font-size: 13px; font-weight: 500; color: var(--ink); height: 40px; }
  .service-menu li.is-current { color: var(--cyan); display: flex; gap: 13px; }
  .service-menu li.is-current::before {
    content: ""; width: 18px; height: 2px; background: var(--cyan); margin-top: 8px;
  }
  .accent-field {
    position: absolute; left: 986px; top: 456px; width: 124px; height: 358px;
    background: linear-gradient(180deg, var(--accent-field) 0%, rgba(227, 229, 238, 0) 100%);
  }
  .service-title {
    position: absolute; left: 470px; top: 462px; font-size: 35px; font-weight: 600;
    line-height: 42px; color: var(--ink);
    background: linear-gradient(transparent 78%, var(--cyan-soft) 78%);
  }
  .service-photo {
    position: absolute; left: 469px; top: 528px; width: 592px; height: 372px;
    background: linear-gradient(160deg, var(--photo-mid) 0%, #34495f 40%, var(--photo-dark) 100%);
  }
</style>
</head>
<body>
  <header class="site-header">
    <div class="brand"><span class="brand-dot"></span>nexora.</div>
    <nav class="main-nav">
      <div class="nav-item" style="left:268px">Home <svg viewBox="0 0 9 6"><path d="M1 1l3.5 3.5L8 1" fill="none" stroke="currentColor" stroke-width="1.3"/></svg></div>
      <div class="nav-item" style="left:368px">About <svg viewBox="0 0 9 6"><path d="M1 1l3.5 3.5L8 1" fill="none" stroke="currentColor" stroke-width="1.3"/></svg></div>
      <div class="nav-item is-active" style="left:469px">Services <svg viewBox="0 0 9 6"><path d="M1 1l3.5 3.5L8 1" fill="none" stroke="currentColor" stroke-width="1.3"/></svg></div>
      <div class="nav-item" style="left:588px">Pages <svg viewBox="0 0 9 6"><path d="M1 1l3.5 3.5L8 1" fill="none" stroke="currentColor" stroke-width="1.3"/></svg></div>
      <div class="nav-item" style="left:688px">News <svg viewBox="0 0 9 6"><path d="M1 1l3.5 3.5L8 1" fill="none" stroke="currentColor" stroke-width="1.3"/></svg></div>
      <div class="nav-item" style="left:786px">Contact</div>
    </nav>
    <svg class="search-icon" viewBox="0 0 15 15"><circle cx="6" cy="6" r="4.6" fill="none" stroke="#222631" stroke-width="2"/><path d="M9.5 9.5L13.5 13.5" stroke="#222631" stroke-width="2.2" stroke-linecap="round"/></svg>
    <div class="quote-button">Get Quote</div>
  </header>

  <section class="hero" role="img" aria-label="Photo of hands working on a laptop keyboard on a dark desk"></section>
  <div class="hero-title-box">
    <h1 class="hero-title">Managed IT-Services</h1>
    <div class="breadcrumb">Home<span>/</span>Managed IT-Services</div>
  </div>

  <aside class="service-menu">
    <h2>Type of Services</h2>
    <ul>
      <li class="is-current">Managed IT-Services</li>
      <li>Multi-function Services</li>
      <li>Cyber Security</li>
      <li>Data Management</li>
      <li>Cloud Computing</li>
      <li>IT Consultancy</li>
    </ul>
  </aside>

  <div class="accent-field" role="img" aria-label="Decorative background pattern area"></div>
  <h2 class="service-title">Managed IT-Services</h2>
  <div class="service-photo" role="img" aria-label="Photo of a person with headphones working on a laptop in a café"></div>
</body>
</html>
```